Chinese restaurant menu and simple logo

We need a menu design for our Chinese fast food restaurant called "Willow Lantern." We are a small take out Chinese restaurant that has limited seating. Most customers order for take-out. The restaurant has been in business for over 20 years and we need a refresh in our menu as well as logo. This restaurant has always been family run and we have many loyal customers so I would like to keep the feeling of a small business run by a family to serve your family.

For the menu:
We would like to see the colors red, yellow, and whites. I have included a menu mockup we have done but it is lacking design. I have also included pictures of the food we have taken which I would like to see some integrated into the menu. I have also included a reference/sample menu that I think should be the direction we should go in terms of design.

The menu is a trifold so it should be divided into 3 sections with each section being 8.5" x 3.6667" so the total size of the menu unfolded is the standard 8.5" x 11" letter size.

For the logo:
The original logo was just the pagoda picture from the chinese take out boxes sold everywhere with the text "Willow Lantern" above it. For the redesigned logo, we would like to keep the pagoda theme but maybe just do a silhouette of the pagoda and integrate the restaurant name "Willow Lantern" into the logo. I have included reference images of pagodas as well. I like the shape of the pagoda from file pagoda_shape.jpg. Which is a more modern silhouette of a pagoda.
Updates

Hi Designers,

I wasn't able to upload all the food photos onto the ArtHive website so I uploaded it to my dropbox: https://www.filebinny.net/sh/x4kvrpl2mtqzd/Ab3Xy9LkQe

Target Market(s)

In the area of our restaurant, we serve mostly to individuals from local businesses and city hall employees for lunch and families for dinner. The demographics are mostly African American and Hispanic.

Industry/Entity Type

Fast Food Restaurant

Requirements
Must have
• The menu should be sized 8.5 inches x 11 inches unfolded. It is a tri-fold so when folded up it will be 8.5" x 3.6667".

Please use the text from files:

Pictures:
Please use pictures from my photo food library at the link here: https://www.filebinny.net/sh/x4kvrpl2mtqzd/Ab3Xy9LkQe

```html
<!DOCTYPE html>
<html lang="en">
<head>
<meta charset="utf-8">
<title>Menu</title>
<link href="https://fonts.googleapis.com/css2?family=PT+Sans:ital,wght@0,400;0,700;1,400&display=swap" rel="stylesheet">
<style>
:root{
  --bg-top:#dc8a2e;
  --bg-mid:#c85a2c;
  --bg-bottom:#b13a2c;
  --glow:#f6cf4a;
  --frame:#f3d22a;
  --text:#ffffff;
  --spicy:#e0262a;
  --photo-a:#7a4a2a;
  --photo-b:#e0b060;
}
*{margin:0;padding:0;box-sizing:border-box}
html,body{width:1200px;height:840px;overflow:hidden}
body{
  position:relative;
  font-family:"PT Sans",sans-serif;
  color:var(--text);
  background:
    radial-gradient(ellipse 380px 320px at 1080px 40px, rgba(246,207,74,.75), rgba(246,207,74,0) 70%),
    linear-gradient(180deg,var(--bg-top) 0%,var(--bg-mid) 50%,var(--bg-bottom) 100%);
}
.frame{
  position:absolute;left:20px;top:22px;width:1160px;height:796px;
  border:18px solid var(--frame);
}
.col{position:absolute}
.col-left{left:53px;width:327px}
.col-mid{left:440px;width:320px}
.col-right{left:815px;width:343px}
.section{position:absolute;left:0;right:0}
.heading{font-weight:700;font-size:16px;text-align:center;line-height:20px;text-transform:uppercase}
.heading .sub{text-transform:none}
.row{display:flex;align-items:baseline;height:19px;font-size:11px;font-weight:700;white-space:nowrap}
.name{flex:none}
.lead{flex:1;border-bottom:1px dotted rgba(255,255,255,.85);margin:0 3px;transform:translateY(-3px)}
.p{flex:none;text-align:left}
.p.side{width:34px}
.p.pint{width:37px}
.p.quart{width:28px}
.price{flex:none;text-align:right}
.cols-head{display:flex;justify-content:flex-end;font-size:11px;font-weight:700;height:17px}
.note{font-size:11px;font-weight:700;height:19px;line-height:19px;white-space:nowrap}
.photo{
  position:absolute;border:3px solid #f4ece4;border-radius:8px;
  background:linear-gradient(90deg,var(--photo-a),#c89060 40%,var(--photo-b) 75%,#e8c890);
}
.photo.bottom{background:linear-gradient(135deg,#e8cf98,#c0452a 45%,#8a2a1c 80%)}
.footnote{position:absolute;right:62px;text-align:right;font-size:10px;line-height:13px}
.footnote .spicy{color:var(--spicy);font-weight:700}
.footnote em{font-style:italic}
</style>
</head>
<body>
<div class="frame" role="img" aria-label="Yellow key-pattern border"></div>

<div class="col col-left">
  <section class="section" style="top:52px">
    <h2 class="heading">Rice</h2>
    <div class="cols-head" style="margin-top:4px"><span class="p pint">Pint</span><span class="p quart">Quart</span></div>
    <div class="row"><span class="name">Beef Fried Rice</span><span class="lead"></span><span class="p pint">4.49</span><span class="p quart">6.29</span></div>
    <div class="row"><span class="name">Chicken Fried Rice</span><span class="lead"></span><span class="p pint">4.49</span><span class="p quart">6.29</span></div>
    <div class="row"><span class="name">Pork Fried Rice</span><span class="lead"></span><span class="p pint">4.49</span><span class="p quart">6.29</span></div>
    <div class="row"><span class="name">Shrimp Fried Rice</span><span class="lead"></span><span class="p pint">5.99</span><span class="p quart">7.99</span></div>
    <div class="row"><span class="name">House Special Fried Rice</span><span class="lead"></span><span class="p quart">7.99</span></div>
    <div class="row"><span class="name">Vegetable Fried Rice</span><span class="lead"></span><span class="p quart">5.59</span></div>
    <div class="row"><span class="name">Steam Rice (side order 1.29)</span><span class="lead"></span><span class="p pint">2.29</span><span class="p quart">3.59</span></div>
  </section>

  <section class="section" style="top:246px">
    <h2 class="heading">A la Carte <span class="sub">(From Steam Table)</span></h2>
    <div class="cols-head"><span class="p side">Side</span><span class="p pint">Pint</span><span class="p quart">Quart</span></div>
    <div class="row"><span class="name">Pan Fried Rice</span><span class="lead"></span><span class="p side">1.79</span><span class="p pint">2.69</span><span class="p quart">4.59</span></div>
    <div class="row"><span class="name">Chow Mein</span><span class="lead"></span><span class="p side">1.99</span><span class="p pint">3.29</span><span class="p quart">4.99</span></div>
    <div class="row"><span class="name">Chow Fun</span><span class="lead"></span><span class="p side">2.19</span><span class="p pint">3.29</span><span class="p quart">5.29</span></div>
    <div class="row"><span class="name">Sweet &amp; Sour Pork</span><span class="lead"></span><span class="p side">2.39</span><span class="p pint">4.39</span><span class="p quart">6.99</span></div>
    <div class="row"><span class="name">Sweet &amp; Sour Chicken</span><span class="lead"></span><span class="p side">2.39</span><span class="p pint">4.39</span><span class="p quart">6.99</span></div>
    <div class="row"><span class="name">Stir Fried Vegetables</span><span class="lead"></span><span class="p side">2.19</span><span class="p pint">3.29</span><span class="p quart">5.29</span></div>
    <div class="row"><span class="name">Cha-Siu (BBQ Pork)</span><span class="lead"></span><span class="p side">2.59</span><span class="p pint">4.59</span><span class="p quart">8.29</span></div>
    <div class="row"><span class="name">Chicken Wings (Fried)</span><span class="lead"></span><span class="p side">2.39</span><span class="p pint">4.39</span><span class="p quart">6.99</span></div>
    <div class="row"><span class="name">Chicken Wings (Stew)</span><span class="lead"></span><span class="p side">2.39</span><span class="p pint">4.39</span><span class="p quart">6.99</span></div>
    <div class="row"><span class="name">Spicy Pork Rib *</span><span class="lead"></span><span class="p side">2.39</span><span class="p pint">4.39</span><span class="p quart">6.99</span></div>
    <div class="row"><span class="name">Mushroom Chicken</span><span class="lead"></span><span class="p side">2.39</span><span class="p pint">4.39</span><span class="p quart">6.99</span></div>
    <div class="row"><span class="name">Orange Chicken</span><span class="lead"></span><span class="p side">2.39</span><span class="p pint">4.39</span><span class="p quart">6.99</span></div>
    <div class="row"><span class="name">String Bean Chicken</span><span class="lead"></span><span class="p side">2.39</span><span class="p pint">4.39</span><span class="p quart">6.99</span></div>
    <div class="row"><span class="name">Kung Pao Chicken *</span><span class="lead"></span><span class="p side">2.39</span><span class="p pint">4.39</span><span class="p quart">6.99</span></div>
    <div class="row"><span class="name">Teriyaki Chicken</span><span class="lead"></span><span class="p side">2.39</span><span class="p pint">4.39</span><span class="p quart">6.99</span></div>
    <div class="row"><span class="name">Broccoli Beef</span><span class="lead"></span><span class="p side">2.39</span><span class="p pint">4.39</span><span class="p quart">6.99</span></div>
    <div class="row"><span class="name">Shrimp Broccoli</span><span class="lead"></span><span class="p side">2.39</span><span class="p pint">4.39</span><span class="p quart">6.99</span></div>
  </section>

  <section class="section" style="top:636px">
    <h2 class="heading">House Specials</h2>
    <div class="row" style="margin-top:6px"><span class="name">Dragon and Phoenix *</span><span class="lead"></span><span class="price">7.29</span></div>
    <div class="note">(A classic combination of shrimp and chicken mixed with an</div>
    <div class="note">abundance of vegetables in a semi-sweet,semi-spicy sauce)</div>
    <div class="row"><span class="name">House Special Vegetables</span><span class="lead"></span><span class="price">7.59</span></div>
    <div class="note">(Chicken, pork, and shrimp stir fried with vegetables)</div>
    <div class="row"><span class="name">Sauteed Shrimp</span><span class="lead"></span><span class="price">9.29</span></div>
    <div class="row"><span class="name">Creamy Shrimp</span><span class="lead"></span><span class="price">(16 pc) 6.29 (25 pc) 9.29</span></div>
  </section>
</div>

<div class="col col-mid">
  <div class="photo" style="top:55px;left:0;width:322px;height:106px" role="img" aria-label="Photo of three dishes: fried chicken wings, shrimp with broccoli and creamy shrimp"></div>

  <section class="section" style="top:177px">
    <h2 class="heading">Chow Mein<br><span class="sub">(Mixed with Bean Sprouts and Noodles)</span></h2>
    <div style="margin-top:6px">
    <div class="row"><span class="name">Beef Chow Mein</span><span class="lead"></span><span class="price">6.59</span></div>
    <div class="row"><span class="name">Chicken Chow Mein</span><span class="lead"></span><span class="price">6.59</span></div>
    <div class="row"><span class="name">Pork Chow Mein</span><span class="lead"></span><span class="price">6.59</span></div>
    <div class="row"><span class="name">Shrimp Chow Mein</span><span class="lead"></span><span class="price">7.59</span></div>
    <div class="row"><span class="name">Vegetable Chow Mein</span><span class="lead"></span><span class="price">5.59</span></div>
    <div class="row"><span class="name">House Special Chow Mein</span><span class="lead"></span><span class="price">7.59</span></div>
    </div>
  </section>

  <section class="section" style="top:343px">
    <h2 class="heading">Chow Fun &amp; Lo Mein</h2>
    <div style="margin-top:4px">
    <div class="row"><span class="name">Beef Chow Fun or Lo Mein</span><span class="lead"></span><span class="price">7.50</span></div>
    <div class="row"><span class="name">Chicken Chow Fun or Lo Mein</span><span class="lead"></span><span class="price">6.99</span></div>
    <div class="row"><span class="name">Pork Chow Fun or Lo Mein</span><span class="lead"></span><span class="price">6.99</span></div>
    <div class="row"><span class="name">Shrimp Chow Fun or Lo Mein</span><span class="lead"></span><span class="price">7.99</span></div>
    <div class="row"><span class="name">House Special Chow Fun or Lo Mein</span><span class="lead"></span><span class="price">7.99</span></div>
    </div>
  </section>

  <section class="section" style="top:466px">
    <h2 class="heading">Soup</h2>
    <div style="margin-top:3px">
    <div class="row"><span class="name">Hot &amp; Sour Soup *</span><span class="lead"></span><span class="price">4.99</span></div>
    <div class="row"><span class="name">Egg Flower Soup</span><span class="lead"></span><span class="price">4.50</span></div>
    <div class="row"><span class="name">Chinese Vegetable Soup</span><span class="lead"></span><span class="price">4.50</span></div>
    <div class="row"><span class="name">Wonton Soup</span><span class="lead"></span><span class="price">4.99</span></div>
    <div class="row"><span class="name">Wor Wonton Soup</span><span class="lead"></span><span class="price">5.99</span></div>
    <div class="row"><span class="name">Pork Noodle Soup</span><span class="lead"></span><span class="price">4.99</span></div>
    <div class="row"><span class="name">Chicken Noodle Soup</span><span class="lead"></span><span class="price">4.99</span></div>
    <div class="row"><span class="name">Beef Noodle Soup</span><span class="lead"></span><span class="price">4.99</span></div>
    <div class="row"><span class="name">Shrimp Noodle Soup</span><span class="lead"></span><span class="price">5.99</span></div>
    </div>
  </section>

  <section class="section" style="top:662px">
    <h2 class="heading">Appetizers</h2>
    <div style="margin-top:3px">
    <div class="row"><span class="name">Egg Roll (Pork and Vegatable) (1)</span><span class="lead"></span><span class="price">1.99</span></div>
    <div class="row"><span class="name">Egg Roll (Vegetable) (2)</span><span class="lead"></span><span class="price">1.79</span></div>
    <div class="row"><span class="name">Egg Foo Young (1)</span><span class="lead"></span><span class="price">1.49</span></div>
    <div class="row"><span class="name">Fried Shrimp (10)</span><span class="lead"></span><span class="price">6.99</span></div>
    <div class="row"><span class="name">Pork Fried Wonton (12)</span><span class="lead"></span><span class="price">5.29</span></div>
    </div>
  </section>
</div>

<div class="col col-right">
  <section class="section" style="top:51px">
    <h2 class="heading">Chicken</h2>
    <div style="margin-top:3px">
    <div class="row"><span class="name">Chinese Black Pepper Chicken</span><span class="lead"></span><span class="price">7.99</span></div>
    <div class="row"><span class="name">Cashew Chicken</span><span class="lead"></span><span class="price">6.99</span></div>
    <div class="row"><span class="name">Curry Chicken *</span><span class="lead"></span><span class="price">6.99</span></div>
    <div class="row"><span class="name">Broccoli Chicken</span><span class="lead"></span><span class="price">6.99</span></div>
    <div class="row"><span class="name">Bell Pepper Chicken</span><span class="lead"></span><span class="price">6.99</span></div>
    <div class="row"><span class="name">Bok Choy Chicken</span><span class="lead"></span><span class="price">6.99</span></div>
    <div class="row"><span class="name">Chicken Chop Suey</span><span class="lead"></span><span class="price">6.99</span></div>
    <div class="row"><span class="name">Chinese Sesame Chicken *</span><span class="lead"></span><span class="price">7.29</span></div>
    <div class="row"><span class="name">Almond Chicken</span><span class="lead"></span><span class="price">6.99</span></div>
    </div>
  </section>

  <section class="section" style="top:259px">
    <h2 class="heading">Beef</h2>
    <div style="margin-top:1px">
    <div class="row"><span class="name">Mandarin Beef *</span><span class="lead"></span><span class="price">7.99</span></div>
    <div class="row"><span class="name">Beef with Oyster Sauce</span><span class="lead"></span><span class="price">7.99</span></div>
    <div class="row"><span class="name">Bell Pepper Beef</span><span class="lead"></span><span class="price">7.99</span></div>
    <div class="row"><span class="name">Bok Choy Beef</span><span class="lead"></span><span class="price">7.99</span></div>
    <div class="row"><span class="name">Orange Beef</span><span class="lead"></span><span class="price">8.50</span></div>
    </div>
  </section>

  <section class="section" style="top:377px">
    <h2 class="heading">Shrimp</h2>
    <div style="margin-top:3px">
    <div class="row"><span class="name">Kung Pao Shrimp *</span><span class="lead"></span><span class="price">7.99</span></div>
    <div class="row"><span class="name">Shrimp with Lobster Sauce</span><span class="lead"></span><span class="price">7.99</span></div>
    <div class="row"><span class="name">Shrimp with Black Bean Sauce</span><span class="lead"></span><span class="price">7.99</span></div>
    <div class="row"><span class="name">Shrimp with Vegetables</span><span class="lead"></span><span class="price">7.99</span></div>
    <div class="row"><span class="name">Garlic Shrimp *</span><span class="lead"></span><span class="price">7.99</span></div>
    <div class="row"><span class="name">Curry Shrimp *</span><span class="lead"></span><span class="price">7.99</span></div>
    <div class="row"><span class="name">Almond Shrimp</span><span class="lead"></span><span class="price">7.99</span></div>
    <div class="row"><span class="name">Orange Shrimp</span><span class="lead"></span><span class="price">8.50</span></div>
    <div class="row"><span class="name">Bok Choy Shrimp</span><span class="lead"></span><span class="price">7.99</span></div>
    <div class="row"><span class="name">Sweet &amp; Sour Shrimp</span><span class="lead"></span><span class="price">7.99</span></div>
    </div>
  </section>
</div>

<div class="photo bottom" style="top:606px;left:838px;width:300px;height:125px" role="img" aria-label="Photo of glazed orange chicken with vegetables over noodles"></div>

<div class="footnote" style="top:741px">
  <div class="spicy">* Hot &amp; Spicy</div>
  <div><em>Prices subject to change without notice</em></div>
</div>
</body>
</html>
```